Business Cards and others
Business cards, stationery, Powerpoint template and E-mail Header and Footer
Professional
Darian Lutrell
CEO
4827 Thornwick Ln
Fenwick Hollow MD 20999
darian@velmorix.com
www.velmorix.com

```html
<!DOCTYPE html>
<html lang="en">
<head>
<meta charset="utf-8">
<title>Velmorix business cards</title>
<link rel="stylesheet" href="https://fonts.googleapis.com/css2?family=Open+Sans:wght@400;600;700&display=swap">
<style>
:root{
  --canvas:#dcd8d1;
  --card-white:#ffffff;
  --card-frost:rgba(255,255,255,0.42);
  --brand:#2a7fcc;
  --band-top:#3a78c4;
  --band-mid:#1d4f9c;
  --band-deep:#123a7a;
  --silver:#c9ced6;
  --ink-light:#ffffff;
}
*{margin:0;padding:0;box-sizing:border-box}
html,body{width:1200px;height:730px;overflow:hidden}
body{background:var(--canvas);font-family:"Open Sans",Arial,sans-serif;position:relative}
.card{position:absolute;width:510px;height:255px;border-radius:16px;overflow:hidden;background:var(--card-white);box-shadow:0 6px 18px rgba(0,0,0,0.18)}
.card--frost{background:var(--card-frost);box-shadow:0 4px 14px rgba(0,0,0,0.10);border:1px solid rgba(255,255,255,0.7)}
.card--front-a{left:72px;top:65px}
.card--front-b{left:667px;top:65px}
.card--back-a{left:72px;top:408px}
.card--back-b{left:667px;top:408px}
.brand{position:absolute;left:0;right:0;top:38px;display:flex;align-items:center;justify-content:center;gap:12px}
.brand__dot{width:46px;height:46px;border-radius:50%;background:var(--brand)}
.brand__name{font-size:34px;font-weight:600;color:var(--brand);letter-spacing:-0.5px}
.card--back-a .brand,.card--back-b .brand{top:34px}
.brand--mirrored{transform:scaleX(-1);opacity:0.45}
.band{position:absolute;left:0;right:0;top:140px;bottom:0;background:linear-gradient(180deg,var(--band-top) 0%,var(--band-mid) 38%,var(--band-deep) 100%);border-top:4px solid var(--silver)}
.band--back{top:118px}
.card--frost .band{opacity:0.9}
.band__name{position:absolute;left:0;right:0;top:8px;text-align:center;font-size:11px;font-weight:600;color:var(--ink-light)}
.band__rule{position:absolute;left:0;right:0;top:32px;height:2px;background:rgba(255,255,255,0.35)}
.contacts{position:absolute;left:0;right:0;top:44px;display:flex;flex-wrap:wrap;justify-content:center;gap:5px 14px;padding:0 30px;font-size:9px;color:var(--ink-light)}
.contact{display:flex;align-items:center;gap:4px;white-space:nowrap}
.contact svg{width:10px;height:10px;flex:none}
.web{position:absolute;left:0;right:0;top:82px;text-align:center;font-size:10px;letter-spacing:4px;color:var(--ink-light)}
</style>
</head>
<body>
<svg width="0" height="0" style="position:absolute">
  <symbol id="icon-pin" viewBox="0 0 10 10"><circle cx="5" cy="5" r="5" fill="#fff"/><path d="M5 2.2a1.8 1.8 0 0 0-1.8 1.8c0 1.4 1.8 3.6 1.8 3.6s1.8-2.2 1.8-3.6A1.8 1.8 0 0 0 5 2.2z" fill="#1d4f9c"/></symbol>
  <symbol id="icon-phone" viewBox="0 0 10 10"><circle cx="5" cy="5" r="5" fill="#fff"/><path d="M3.3 2.6l1 1-.5.7a4 4 0 0 0 1.9 1.9l.7-.5 1 1-.7.8C4.8 7.6 2.4 5.2 2.5 3.3z" fill="#1d4f9c"/></symbol>
  <symbol id="icon-globe" viewBox="0 0 10 10"><circle cx="5" cy="5" r="5" fill="#fff"/><circle cx="5" cy="5" r="2.8" fill="none" stroke="#1d4f9c" stroke-width="0.7"/><path d="M2.2 5h5.6M5 2.2c-1.3 1.6-1.3 4 0 5.6M5 2.2c1.3 1.6 1.3 4 0 5.6" fill="none" stroke="#1d4f9c" stroke-width="0.6"/></symbol>
  <symbol id="icon-mail" viewBox="0 0 10 10"><circle cx="5" cy="5" r="5" fill="#fff"/><rect x="2.4" y="3.2" width="5.2" height="3.6" fill="none" stroke="#1d4f9c" stroke-width="0.7"/><path d="M2.4 3.2L5 5.3l2.6-2.1" fill="none" stroke="#1d4f9c" stroke-width="0.7"/></symbol>
</svg>

<section class="card card--front-a">
  <div class="brand"><span class="brand__dot"></span><span class="brand__name">Velmorix</span></div>
  <div class="band">
    <p class="band__name">Darian Lutrell | CEO</p>
    <div class="band__rule"></div>
    <div class="contacts">
      <span class="contact"><svg><use href="#icon-pin"/></svg>4827 Thornwick Ln Ste 2 Fenwick Hollow MD 20999</span>
      <span class="contact"><svg><use href="#icon-globe"/></svg>www.velmorix.com</span>
      <span class="contact"><svg><use href="#icon-phone"/></svg>555-014-2286</span>
      <span class="contact"><svg><use href="#icon-phone"/></svg>555019374</span>
      <span class="contact"><svg><use href="#icon-phone"/></svg>5550176432</span>
      <span class="contact"><svg><use href="#icon-mail"/></svg>darian@velmorix.com</span>
    </div>
  </div>
</section>

<section class="card card--frost card--front-b">
  <div class="brand"><span class="brand__dot"></span><span class="brand__name">Velmorix</span></div>
  <div class="band">
    <p class="band__name">Darian Lutrell | CEO</p>
    <div class="band__rule"></div>
    <div class="contacts">
      <span class="contact"><svg><use href="#icon-pin"/></svg>4827 Thornwick Ln Ste 2 Fenwick Hollow MD 20999</span>
      <span class="contact"><svg><use href="#icon-globe"/></svg>www.velmorix.com</span>
      <span class="contact"><svg><use href="#icon-phone"/></svg>555-014-2286</span>
      <span class="contact"><svg><use href="#icon-phone"/></svg>555019374</span>
      <span class="contact"><svg><use href="#icon-phone"/></svg>5550176432</span>
      <span class="contact"><svg><use href="#icon-mail"/></svg>darian@velmorix.com</span>
    </div>
  </div>
</section>

<section class="card card--back-a">
  <div class="brand"><span class="brand__dot"></span><span class="brand__name">Velmorix</span></div>
  <div class="band band--back"><p class="web">www.velmorix.com</p></div>
</section>

<section class="card card--frost card--back-b">
  <div class="brand brand--mirrored"><span class="brand__dot"></span><span class="brand__name">Velmorix</span></div>
  <div class="band band--back"><p class="web">www.velmorix.com</p></div>
</section>
</body>
</html>
```